Every Drawer Neatly Sorted or EDN Organized needs a business card design. EDN Organized is a professi

We need a business card design that is clean, sharp and conveys a sense of organization. I already have a logo.

Target Market(s)

Families (specifically mothers), small business owners, parents, seniors

Industry/Entity Type

Business

Contact Information for Business Card

My website is www.ednorganized-example.com and my Facebook page is http://www.socialpage-example.com/everydrawerneatlysorted. The phone number is 555-418-2706 and I want to be listed as Miriel O. Dunsford, Owner

Requirements
Must have
• My logo.

```html
<!DOCTYPE html>
<html lang="en">
<head>
<meta charset="utf-8">
<title>EDN Organized — Business Card</title>
<link rel="stylesheet" href="https://fonts.googleapis.com/css2?family=Open+Sans:wght@400;600;700&display=swap">
<style>
  :root {
    --backdrop: #d9d9d9;
    --card: #f4f4f2;
    --ink: #1b1b1b;
    --brand-blue: #2a6db3;
    --rule: #1b1b1b;
  }
  * { box-sizing: border-box; margin: 0; padding: 0; }
  html, body {
    width: 1200px;
    height: 1200px;
    overflow: hidden;
    background: var(--backdrop);
    font-family: "Open Sans", Arial, sans-serif;
    color: var(--ink);
  }
  .stage {
    width: 1200px;
    height: 1200px;
    display: flex;
    align-items: center;
    justify-content: center;
  }
  .business-card {
    width: 900px;
    height: 514px;
    background: var(--card);
    box-shadow: 0 6px 24px rgba(0,0,0,0.12);
    display: flex;
    align-items: center;
    padding: 0 50px 0 70px;
    overflow: hidden;
  }
  .brand {
    flex: 0 0 370px;
    display: flex;
    align-items: center;
    gap: 12px;
    margin-top: -40px;
  }
  .brand-square {
    width: 16px;
    height: 16px;
    background: var(--brand-blue);
    flex: 0 0 auto;
  }
  .brand-name {
    color: var(--brand-blue);
    font-weight: 400;
    font-size: 23px;
    letter-spacing: 0.5px;
    line-height: 1.25;
    white-space: nowrap;
  }
  .divider {
    width: 3px;
    height: 240px;
    background: var(--rule);
    margin: 0 34px 0 22px;
    flex: 0 0 auto;
  }
  .contact-block { flex: 1; min-width: 0; }
  .person-name {
    font-weight: 700;
    font-size: 25px;
    line-height: 1.1;
  }
  .person-role {
    font-size: 20px;
    margin-bottom: 30px;
  }
  .contact-list { list-style: none; }
  .contact-item {
    display: flex;
    align-items: center;
    gap: 11px;
    font-size: 19px;
    line-height: 1.75;
    white-space: nowrap;
  }
  .contact-icon { width: 15px; height: 15px; flex: 0 0 auto; fill: var(--ink); }
  .social-mark { width: 13px; height: 13px; background: var(--ink); border-radius: 2px; flex: 0 0 auto; margin: 0 1px; }
</style>
</head>
<body>
  <main class="stage">
    <section class="business-card">
      <div class="brand">
        <span class="brand-square"></span>
        <span class="brand-name">Every Drawer Neatly Sorted</span>
      </div>
      <div class="divider"></div>
      <div class="contact-block">
        <p class="person-name">Miriel O. Dunsford</p>
        <p class="person-role">Owner</p>
        <ul class="contact-list">
          <li class="contact-item">
            <svg class="contact-icon" viewBox="0 0 24 24" aria-hidden="true"><path d="M6.6 10.8c1.4 2.8 3.8 5.1 6.6 6.6l2.2-2.2c.3-.3.7-.4 1-.2 1.1.4 2.3.6 3.6.6.6 0 1 .4 1 1V20c0 .6-.4 1-1 1C10.6 21 3 13.4 3 4c0-.6.4-1 1-1h3.5c.6 0 1 .4 1 1 0 1.3.2 2.5.6 3.6.1.3 0 .7-.2 1z"/></svg>
            <span>555-418-2706</span>
          </li>
          <li class="contact-item">
            <span class="social-mark" aria-hidden="true"></span>
            <span>everydrawerneatlysorted</span>
          </li>
          <li class="contact-item">
            <svg class="contact-icon" viewBox="0 0 24 24" aria-hidden="true"><circle cx="12" cy="12" r="10"/><path d="M2 12h20M12 2c3 3 3 17 0 20M12 2c-3 3-3 17 0 20" stroke="var(--card)" stroke-width="1.5" fill="none"/></svg>
            <span>www.ednorganized-example.com</span>
          </li>
        </ul>
      </div>
    </section>
  </main>
</body>
</html>
```